Print Ad Design

I need an ad designed to promote an event that we are hosting at a trade show for placement in the show program. The art must be ready to submit to the publication by Friday, November 15th at the latest. The ad is 1/2 page in the show program that will be 4.25"X 5.5" and must be submitted as a high resolution (300dpi) PDF. Ad is full colour. The minimum bleed and trim marks are 0.25". The trade show is the Northern Herd Fair in Canada and we would like to promote a 2 day training we will be hosting at the close of the show. Our company is PastureLink Systems - Ultrasound and Diagnostics and the details that should be included in the ad are:
YOU CAN USE ULTRASOUND TO MANAGE YOUR PREG CHECKS
On Farm Ultrasound Training for Producers
When - Friday, Feb. 7th & Saturday, Feb. 8th
9 AM - 5 PM
Where - close to Herd FAIR
Lunch provided
Registration $175 per day - $300 total
Introduction to ultrasound
Reproductive system anatomy
Pregnancy diagnosis
Live on farm scanning demonstrations and practice with case discussions
Tuition redeemable towards the purchase of ultrasound system.
TO REGISTER OR LEARN MORE
email - info@pasturelinksystems.ca or call 1-800-555-0147
(I have attached our logo and some possible images to use in the ad)
Please note that the primary logo to feature is PastureLink Systems and the secondary logo to use in the ad is Velorek Ultrasound Scanners.
THANK YOU!!!
Target Market(s)
Dairy Farmers (men and women)
Industry/Entity Type
Trade
Look and feel

```html
<!DOCTYPE html>
<html lang="en">
<head>
<meta charset="utf-8">
<title>PastureLink Systems – On Farm Ultrasound Training</title>
<link rel="stylesheet" href="https://fonts.googleapis.com/css2?family=Roboto+Condensed:wght@300;400;700&family=Arimo:wght@400;700&display=swap">
<style>
  :root {
    --navy: #1b4574;
    --navy-dark: #173c66;
    --gold: #f4b81c;
    --ink: #1e1e1e;
    --paper: #ffffff;
    --stage: #ecebe8;
    --rule: #8a8a8a;
  }
  * { box-sizing: border-box; margin: 0; padding: 0; }
  html, body { width: 993px; height: 1200px; overflow: hidden; }
  body { background: var(--stage); position: relative; font-family: "Arimo", Arial, sans-serif; }

  .ad {
    position: absolute; left: 127px; top: 120px;
    width: 745px; height: 953px; background: var(--paper);
  }
  .ad-frame {
    position: absolute; left: 14px; top: 13px; width: 717px; height: 927px;
    border: 1px solid var(--rule);
  }

  .brand {
    position: absolute; left: 38px; top: 48px;
    display: flex; align-items: center; gap: 12px;
  }
  .brand-mark { width: 46px; height: 46px; border-radius: 50%; background: var(--gold); }
  .brand-name {
    font-family: "Roboto Condensed", sans-serif; font-weight: 400;
    font-size: 40px; color: var(--navy); line-height: 1;
  }
  .brand-tag {
    position: absolute; left: 96px; top: 98px;
    font-family: "Roboto Condensed", sans-serif; font-weight: 400;
    font-size: 15px; color: var(--navy); letter-spacing: 1px;
  }

  .partner {
    position: absolute; left: 498px; top: 44px; width: 211px;
    display: flex; align-items: center; gap: 8px;
  }
  .partner-mark { width: 14px; height: 14px; background: var(--gold); flex: none; }
  .partner-name {
    font-family: "Roboto Condensed", sans-serif; font-weight: 700;
    font-size: 17px; line-height: 1.1; color: var(--navy); text-transform: uppercase;
  }

  .photo { position: absolute; top: 131px; height: 280px; }
  .photo-team { left: 32px; width: 455px; background: linear-gradient(135deg, #3f4a52 0%, #2f4f86 40%, #d9dcde 70%, #5a4a3a 100%); }
  .photo-solo { left: 508px; width: 210px; background: linear-gradient(160deg, #d7d3cc 0%, #5fc3b3 45%, #e8e8e4 75%, #2a2a2a 100%); }

  .headline {
    position: absolute; left: 0; top: 426px; width: 745px; text-align: center;
    font-family: "Roboto Condensed", sans-serif; color: var(--navy);
    font-size: 46px; line-height: 55px; font-weight: 300;
  }
  .headline strong { font-weight: 700; }

  .subhead-band {
    position: absolute; left: 41px; top: 545px; width: 656px; height: 35px;
    background: var(--gold); text-align: center;
    font-weight: 700; font-size: 24px; line-height: 35px; color: var(--ink);
  }

  .details {
    position: absolute; left: 39px; top: 602px; width: 334px; height: 236px;
    background: var(--navy); color: #fff; font-size: 19px; line-height: 24px;
  }
  .details-fold { position: absolute; right: 0; bottom: 0; width: 20px; height: 20px; }
  .detail { position: absolute; left: 20px; display: flex; }
  .detail svg { width: 19px; height: 19px; margin-top: 3px; margin-right: 12px; flex: none; }
  .detail-when { top: 16px; }
  .detail-when .label { width: 85px; }
  .detail-where { top: 99px; }
  .detail-reg { top: 136px; }
  .detail-lunch { top: 197px; }

  .topics {
    position: absolute; left: 396px; top: 602px; width: 320px; list-style: none;
    font-family: "Roboto Condensed", sans-serif; font-size: 23px; line-height: 26px; color: var(--ink);
  }
  .topics li { display: flex; margin-bottom: 7px; }
  .topics svg { width: 22px; height: 22px; margin-right: 12px; margin-top: 1px; flex: none; }
  .tuition {
    position: absolute; left: 407px; top: 789px; width: 320px;
    font-weight: 700; font-size: 19px; line-height: 26px; color: var(--ink);
  }

  .cta {
    position: absolute; left: 33px; top: 862px; width: 230px; text-align: center;
    font-size: 25px; line-height: 32px; color: var(--ink);
  }
  .cta-rule { position: absolute; left: 275px; top: 856px; width: 1px; height: 68px; background: var(--rule); }
  .contact { position: absolute; left: 290px; top: 858px; color: var(--navy); font-weight: 700; }
  .contact-line { display: flex; align-items: center; }
  .contact-phone { font-size: 35px; line-height: 42px; }
  .contact-email { font-size: 24px; line-height: 30px; }
  .contact svg { flex: none; margin-right: 10px; }
</style>
</head>
<body>
  <article class="ad">
    <div class="ad-frame"></div>

    <div class="brand">
      <span class="brand-mark"></span>
      <span class="brand-name">PastureLink Systems</span>
    </div>
    <div class="brand-tag">ultrasound and diagnostics</div>

    <div class="partner">
      <span class="partner-mark"></span>
      <span class="partner-name">Velorek Ultrasound Scanners</span>
    </div>

    <div class="photo photo-team" role="img" aria-label="Two technicians in caps and aprons scanning a dairy cow with handheld ultrasound units"></div>
    <div class="photo photo-solo" role="img" aria-label="Woman in a teal coat performing an ultrasound preg check on a Holstein cow"></div>

    <h1 class="headline">YOU CAN USE <strong>ULTRASOUND</strong><br>TO MANAGE YOUR <strong>PREG CHECKS</strong></h1>

    <div class="subhead-band">On Farm Ultrasound Training for Producers</div>

    <section class="details">
      <div class="detail detail-when">
        <svg viewBox="0 0 20 20"><circle cx="10" cy="10" r="9" fill="none" stroke="#f4b81c" stroke-width="2"/><path d="M5 10h9M10 6l4 4-4 4" fill="none" stroke="#f4b81c" stroke-width="2.2"/></svg>
        <span class="label">When -</span>
        <span>Friday, Feb. 7th &amp;<br>Saturday, Feb. 8th<br>9 AM - 5 PM</span>
      </div>
      <div class="detail detail-where">
        <svg viewBox="0 0 20 20"><circle cx="10" cy="10" r="9" fill="none" stroke="#f4b81c" stroke-width="2"/><path d="M5 10h9M10 6l4 4-4 4" fill="none" stroke="#f4b81c" stroke-width="2.2"/></svg>
        <span>Where - close to Herd FAIR</span>
      </div>
      <div class="detail detail-reg">
        <svg viewBox="0 0 20 20"><circle cx="10" cy="10" r="9" fill="none" stroke="#f4b81c" stroke-width="2"/><path d="M5 10h9M10 6l4 4-4 4" fill="none" stroke="#f4b81c" stroke-width="2.2"/></svg>
        <span>Registration<br>$175 per day - $300 total</span>
      </div>
      <div class="detail detail-lunch">
        <svg viewBox="0 0 20 20"><circle cx="10" cy="10" r="9" fill="none" stroke="#f4b81c" stroke-width="2"/><path d="M5 10h9M10 6l4 4-4 4" fill="none" stroke="#f4b81c" stroke-width="2.2"/></svg>
        <span>Lunch provided</span>
      </div>
      <svg class="details-fold" viewBox="0 0 20 20"><path d="M20 0L0 20H20Z" fill="#ffffff"/><path d="M20 0L0 20V0Z" fill="#f4b81c"/></svg>
    </section>

    <ul class="topics">
      <li><svg viewBox="0 0 22 22"><circle cx="11" cy="11" r="10" fill="#1b4574"/><path d="M6 11l4 4 7-8" fill="none" stroke="#f4b81c" stroke-width="2.6"/></svg>Introduction to ultrasound</li>
      <li><svg viewBox="0 0 22 22"><circle cx="11" cy="11" r="10" fill="#1b4574"/><path d="M6 11l4 4 7-8" fill="none" stroke="#f4b81c" stroke-width="2.6"/></svg>Reproductive system anatomy</li>
      <li><svg viewBox="0 0 22 22"><circle cx="11" cy="11" r="10" fill="#1b4574"/><path d="M6 11l4 4 7-8" fill="none" stroke="#f4b81c" stroke-width="2.6"/></svg>Pregnancy diagnosis</li>
      <li><svg viewBox="0 0 22 22"><circle cx="11" cy="11" r="10" fill="#1b4574"/><path d="M6 11l4 4 7-8" fill="none" stroke="#f4b81c" stroke-width="2.6"/></svg><span>Live on farm scanning demonstrations and practice with case discussions</span></li>
    </ul>
    <p class="tuition">Tuition redeemable towards the purchase of ultrasound system.</p>

    <p class="cta">TO REGISTER<br>OR LEARN MORE</p>
    <div class="cta-rule"></div>
    <div class="contact">
      <div class="contact-line contact-phone">
        <svg width="20" height="30" viewBox="0 0 20 30"><rect x="1" y="1" width="18" height="28" rx="3" fill="#f4b81c"/><rect x="4" y="5" width="12" height="9" fill="#fff"/><rect x="4" y="17" width="12" height="8" fill="#fff" opacity=".6"/></svg>
        <span>1-800-555-0147</span>
      </div>
      <div class="contact-line contact-email">
        <svg width="24" height="16" viewBox="0 0 24 16"><rect width="24" height="16" fill="#f4b81c"/><path d="M0 0l12 9 12-9" fill="none" stroke="#fff" stroke-width="1.6"/></svg>
        <span>info@pasturelinksystems.ca</span>
      </div>
    </div>
  </article>
</body>
</html>
```